Business Card Design Project

I run holistic health workshops, speaking engagements, group and 1on1 coaching, cooking classes, and am a speaker and presenter on holistic health topics.

I would like professionally designed business cards using the attached logo. I would like the reverse of the cards to use the leaf pattern blown up large across the back of the card as the design. I'd also like to use the words "rest.move.breathe.nourish" across the backside of the cards.

The front of the cards should contain the following contact details:
Megan Thorsby-Kell
Founder & President
The Harwick Advisory Group
+61 477 392 604
theharwickadvisorygroup@mailbrook.example

Target Market(s)

Corporate HR, Health & wellness businesses, upmarket spas, other businesses in the holistic health & wellness fields looking for a speaker/presenter/workshop leader

Industry/Entity Type

Cooking

Requirements
Must have
• Must use the attached design; must use earth tones in line with the logo (browns/greens/blues/tans)

```html
<!DOCTYPE html>
<html lang="en">
<head>
<meta charset="utf-8">
<title>The Harwick Advisory Group – Business Card</title>
<link rel="stylesheet" href="https://fonts.googleapis.com/css2?family=Arimo:wght@400;700&display=swap">
<style>
  :root {
    --ink: #4a4a46;
    --ink-band: #4b4b47;
    --paper: #ffffff;
    --leaf-light: #8dc63f;
    --leaf-mid: #39b54a;
    --leaf-deep: #009245;
  }
  html, body {
    margin: 0;
    padding: 0;
    width: 1200px;
    height: 686px;
    overflow: hidden;
    background: var(--paper);
  }
  .card {
    position: relative;
    width: 1200px;
    height: 686px;
    background: var(--paper);
    font-family: "Arimo", Arial, sans-serif;
    color: var(--ink);
    overflow: hidden;
  }
  .brand {
    position: absolute;
    left: 30px;
    top: 70px;
    width: 250px;
  }
  .brand-row {
    display: flex;
    align-items: center;
    gap: 10px;
  }
  .brand-dot {
    width: 34px;
    height: 34px;
    border-radius: 50%;
    background: var(--leaf-light);
    flex: none;
  }
  .brand-name {
    font-weight: 700;
    font-size: 30px;
    line-height: 1;
    color: var(--ink);
    white-space: nowrap;
  }
  .brand-tagline {
    position: absolute;
    left: 38px;
    top: 186px;
    font-size: 16px;
    letter-spacing: 0.3px;
    color: var(--ink);
    white-space: nowrap;
  }
  .title-band {
    position: absolute;
    left: 297px;
    top: 59px;
    width: 886px;
    height: 92px;
    background: var(--ink-band);
    display: flex;
    align-items: center;
    padding-left: 34px;
    box-sizing: border-box;
  }
  .company-name {
    margin: 0;
    font-weight: 400;
    font-size: 56px;
    color: var(--paper);
    white-space: nowrap;
  }
  .leaf-field {
    position: absolute;
    left: 714px;
    top: 166px;
    width: 486px;
    height: 457px;
    background:
      radial-gradient(ellipse at 55% 55%, var(--leaf-deep) 0%, var(--leaf-mid) 35%, rgba(141,198,63,0.55) 62%, rgba(141,198,63,0) 80%);
  }
  .person {
    position: absolute;
    left: 60px;
    top: 328px;
    width: 640px;
    text-align: center;
  }
  .person-name {
    margin: 0;
    font-weight: 700;
    font-size: 52px;
    line-height: 1;
    color: var(--ink);
  }
  .person-role {
    margin: 12px 0 0;
    font-weight: 400;
    font-size: 36px;
    color: var(--ink);
  }
  .contact-band {
    position: absolute;
    left: 0;
    bottom: 0;
    width: 1200px;
    height: 63px;
    background: var(--ink-band);
    display: flex;
    align-items: center;
    justify-content: space-between;
    padding: 0 31px;
    box-sizing: border-box;
    color: var(--paper);
    font-size: 33px;
    white-space: nowrap;
  }
</style>
</head>
<body>
  <main class="card">
    <div class="brand">
      <div class="brand-row">
        <span class="brand-dot"></span>
        <span class="brand-name">Harwick Group</span>
      </div>
    </div>
    <div class="brand-tagline">rest.move.breathe.nourish</div>

    <header class="title-band">
      <h1 class="company-name">The Harwick Advisory Group</h1>
    </header>

    <div class="leaf-field" role="img" aria-label="Large soft green decorative area"></div>

    <section class="person">
      <h2 class="person-name">Megan Thorsby-Kell</h2>
      <p class="person-role">Founder &amp; President</p>
    </section>

    <footer class="contact-band">
      <span class="contact-phone">+61 477 392 604</span>
      <span class="contact-email">theharwickadvisorygroup@mailbrook.example</span>
    </footer>
  </main>
</body>
</html>
```